Redesigning of the packaging for 4 MORNING VELVET gourmet breads

We need new designs for our range of four gourmet sliced breads, called MORNING VELVET. These breads are prepared with specially selected ingredients sourced from several countries and with extreme focus on quality, health and indulgent pleasure. The Morning Velvet brand aims to solve the boring and bland nature of white breads and comes in several flavours such as coconut, seeds & nuts, exotic fruits and vegetables, buttermilk, chocolate, etc.
The Morning Velvet brand positioning statement is JOY IN EVERY SLICE
The current packaging designs are still quite attractive which makes it a difficult decision, but we know it's time for a rebrand, and therefore we really want the best possible designs - ONLY THE BEST!
MORNING VELVET currently comprises three 'sister' products and one new addition named as follows:
1. Morning Velvet - buttermilk bliss (yellow color)
2. Morning Velvet - choco delight (brown & orange color)
3. Morning Velvet - creamy coconut (green & cream color)
4. Morning Totz - (kiddies' style - This is a kiddies bread)
[Some pictures of the current packaging are attached, alongside with the content, layout and dimensions which should be used for the new designs, including ingredients, addresses, etc. Check the file 'Back view with ingredients and contents.pdf'; 'Layout and Dimensions of current Morning Velvet Packaging.pdf]
5. The logo may or may not be modified. (Morning Velvet Logo.pdf)
Key points to note:
- Demographic: The target audience is mainly young and middle aged from the middle to upper economic class
- Psychographic: Health conscious, Class conscious, Family focused consumers, Environment and Sustainable development minded consumers
- The designs will be similar in style for the 3 variants but be differentiated by colours and content
- The fonts and the overall design should be modern, playful and inviting.
- The content of the packaging is in the attachments
- Total designs - 4 designs.
Target Market(s)
The target market is kids, teens, young adults. Middle to upper economic class. Premium segment, lifestyle conscious consumers.
Industry/Entity Type
Bakery
Colors
Designer to choose colors to be used in the design.
Look and feel
Each slider illustrates characteristics of the customer's brand and the style your logo design should communicate.

```html
<!DOCTYPE html>
<html lang="en">
<head>
<meta charset="UTF-8">
<title>Morning Velvet – Pack Labels</title>
<link rel="stylesheet" href="https://fonts.googleapis.com/css2?family=Nunito:ital,wght@0,800;0,900;1,800&display=swap">
<style>
  :root {
    --buttermilk: #facb05;
    --choco-start: #f39322;
    --choco-end: #8a3a3a;
    --coconut-start: #d6eacb;
    --coconut-end: #7fc03e;
    --kiddies-start: #f7c3d0;
    --kiddies-end: #c9e298;
    --brand-red: #c4101e;
    --brand-blue: #009fe3;
    --olive: #7a6410;
    --tagline-olive: #8a6d0c;
    --kiddies-pink: #ef4b6e;
    --white: #ffffff;
  }
  * { margin: 0; padding: 0; box-sizing: border-box; }
  html, body { width: 1200px; height: 1200px; overflow: hidden; }
  body { font-family: "Nunito", sans-serif; }

  .label-sheet { width: 1200px; height: 1200px; display: flex; flex-direction: column; }
  .label-band { position: relative; height: 300px; }

  .band-buttermilk { background: var(--buttermilk); }
  .band-choco { background: linear-gradient(90deg, var(--choco-start) 5%, var(--choco-end) 100%); }
  .band-coconut { background: linear-gradient(90deg, var(--coconut-start) 5%, var(--coconut-end) 100%); }
  .band-kiddies { background: linear-gradient(90deg, var(--kiddies-start) 5%, var(--kiddies-end) 100%); }

  .brand-block {
    position: absolute; left: 110px; top: 30px; width: 350px; height: 250px;
    text-align: center;
  }
  .brand-glow {
    position: absolute; left: 20px; top: 0; width: 310px; height: 200px;
    background: radial-gradient(ellipse at center, rgba(255,255,255,0.55) 0%, rgba(255,255,255,0) 68%);
  }
  .brand-name {
    position: relative; padding-top: 28px;
    font-weight: 900; font-size: 58px; line-height: 58px; letter-spacing: 1px;
  }
  .name-red { color: var(--brand-red); }
  .name-blue { color: var(--brand-blue); }
  .brand-tagline {
    position: relative; margin-top: 14px;
    font-weight: 800; font-size: 12px; letter-spacing: 4px;
    color: var(--tagline-olive);
  }
  .tagline-light { color: var(--white); }
  .flavour-name {
    position: relative; margin-top: 12px;
    font-weight: 800; font-style: italic; font-size: 29px; letter-spacing: 1.5px;
  }
  .flavour-white { color: var(--white); }
  .flavour-olive { color: var(--olive); }
  .flavour-pink { color: var(--kiddies-pink); }

  .window-frame {
    position: absolute; left: 564px; top: 50px; width: 525px; height: 200px;
    border: 3px solid var(--white); border-radius: 64px;
  }
  .window-panel {
    position: absolute; left: 575px; top: 60px; width: 504px; height: 180px;
    background: var(--white); border-radius: 46px;
  }
  .side-tab {
    position: absolute; left: 1108px; top: 61px; width: 33px; height: 182px;
    background: var(--white); border-radius: 17px;
  }
</style>
</head>
<body>
<main class="label-sheet">

  <section class="label-band band-buttermilk">
    <div class="brand-block">
      <div class="brand-glow"></div>
      <div class="brand-name name-red">MORNING<br>VELVET</div>
      <div class="brand-tagline">CREAMY BREAKFAST DELIGHT</div>
      <div class="flavour-name flavour-white">buttermilk bliss</div>
    </div>
    <div class="window-frame"></div>
    <div class="window-panel"></div>
    <div class="side-tab"></div>
  </section>

  <section class="label-band band-choco">
    <div class="brand-block">
      <div class="brand-glow"></div>
      <div class="brand-name name-blue">MORNING<br>VELVET</div>
      <div class="brand-tagline tagline-light">CREAMY BREAKFAST DELIGHT</div>
      <div class="flavour-name flavour-white">choco delight</div>
    </div>
    <div class="window-frame"></div>
    <div class="window-panel"></div>
    <div class="side-tab"></div>
  </section>

  <section class="label-band band-coconut">
    <div class="brand-block">
      <div class="brand-glow"></div>
      <div class="brand-name name-red">MORNING<br>VELVET</div>
      <div class="brand-tagline">CREAMY BREAKFAST DELIGHT</div>
      <div class="flavour-name flavour-olive">creamy coconut</div>
    </div>
    <div class="window-frame"></div>
    <div class="window-panel"></div>
    <div class="side-tab"></div>
  </section>

  <section class="label-band band-kiddies">
    <div class="brand-block">
      <div class="brand-glow"></div>
      <div class="brand-name name-blue">MORNING<br>VELVET</div>
      <div class="brand-tagline">CREAMY BREAKFAST DELIGHT</div>
      <div class="flavour-name flavour-pink">kiddies' style</div>
    </div>
    <div class="window-frame"></div>
    <div class="window-panel"></div>
    <div class="side-tab"></div>
  </section>

</main>
</body>
</html>
```